Property Management Company looking for a high-end business card, letterhead and envelope design.

We provide high-end / boutique property management for real estate investors or individuals looking for someone to manage their portfolio. we are looking for a cohesive high-end design for our business cards, letterhead and envelopes.

Target Market(s)

Real Estate Investors

Industry/Entity Type

Real Estate

Requirements
Must have
• business card, letterhead and envelope design - logo attached

```html
<!DOCTYPE html>
<html lang="en">
<head>
<meta charset="UTF-8">
<title>Northvale Property Management – Stationery</title>
<link href="https://fonts.googleapis.com/css2?family=Montserrat:wght@400;600&display=swap" rel="stylesheet">
<style>
  :root {
    --bg: #c6c6c6;
    --paper: #ffffff;
    --blue: #024b85;
    --navy: #023059;
    --grey: #bdbdbd;
  }
  html, body {
    margin: 0;
    padding: 0;
    width: 1200px;
    height: 900px;
    overflow: hidden;
    background: var(--bg);
    font-family: "Montserrat", sans-serif;
  }
  .canvas {
    position: relative;
    width: 1200px;
    height: 900px;
  }
  .piece {
    position: absolute;
    overflow: hidden;
    background: var(--paper);
  }
  .accent-area {
    position: absolute;
  }
  .brand {
    position: absolute;
    line-height: 1;
  }
  .brand-name {
    display: block;
    font-weight: 600;
    letter-spacing: 0.2em;
    white-space: nowrap;
  }
  .brand-tag {
    display: block;
    font-weight: 400;
    letter-spacing: 0.22em;
    white-space: nowrap;
  }

  /* Business card – front */
  .card-front {
    left: 90px; top: 59px; width: 280px; height: 155px;
    background: var(--blue);
  }
  .card-front .brand { left: 30px; top: 55px; color: var(--paper); }
  .card-front .brand-name { font-size: 26px; }
  .card-front .brand-tag { font-size: 12px; margin-top: 5px; letter-spacing: 0.2em; }

  /* Business card – back */
  .card-back { left: 93px; top: 225px; width: 277px; height: 154px; }
  .card-back .accent-area {
    left: 0; top: 0; width: 62px; height: 100%;
    background: linear-gradient(180deg, var(--blue), var(--navy));
  }
  .card-back .brand { left: 93px; top: 65px; }
  .card-back .brand-name { font-size: 18px; color: var(--navy); }
  .card-back .brand-tag { font-size: 9px; margin-top: 4px; color: var(--blue); }

  /* Letterhead */
  .letterhead { left: 399px; top: 59px; width: 551px; height: 779px; }
  .letterhead .accent-area {
    left: 0; top: 0; width: 62px; height: 100%;
    background: linear-gradient(180deg, var(--blue), var(--navy));
  }
  .letterhead .brand { left: 106px; top: 62px; }
  .letterhead .brand-name { font-size: 21px; color: var(--navy); }
  .letterhead .brand-tag { font-size: 9px; margin-top: 4px; color: var(--blue); }

  /* Envelope */
  .envelope { left: 142px; top: 390px; width: 583px; height: 292px; }
  .envelope .accent-area {
    left: 0; bottom: 0; width: 100%; height: 118px;
    background: linear-gradient(90deg, var(--blue), var(--navy));
  }
  .envelope .brand { right: 13px; top: 240px; color: var(--paper); text-align: right; }
  .envelope .brand-name { font-size: 21px; }
  .envelope .brand-tag { font-size: 10px; margin-top: 4px; letter-spacing: 0.2em; }
</style>
</head>
<body>
<main class="canvas">

  <section class="piece card-front" aria-label="Business card front">
    <div class="brand">
      <span class="brand-name">NORTHVALE</span>
      <span class="brand-tag">PROPERTY MANAGEMENT</span>
    </div>
  </section>

  <section class="piece card-back" aria-label="Business card back">
    <div class="accent-area" role="img" aria-label="Blue and navy decorative area along the left edge"></div>
    <div class="brand">
      <span class="brand-name">NORTHVALE</span>
      <span class="brand-tag">PROPERTY MANAGEMENT</span>
    </div>
  </section>

  <section class="piece letterhead" aria-label="Letterhead">
    <div class="accent-area" role="img" aria-label="Blue and navy decorative strip along the left edge"></div>
    <div class="brand">
      <span class="brand-name">NORTHVALE</span>
      <span class="brand-tag">PROPERTY MANAGEMENT</span>
    </div>
  </section>

  <section class="piece envelope" aria-label="Envelope">
    <div class="accent-area" role="img" aria-label="Blue and navy decorative band along the bottom edge"></div>
    <div class="brand">
      <span class="brand-name">NORTHVALE</span>
      <span class="brand-tag">PROPERTY MANAGEMENT</span>
    </div>
  </section>

</main>
</body>
</html>
```